Wine Bottle Label Logo Design

My fiancé and I are getting married in September and we made homemade wine which will be given to the guests as a wedding favor. We need label/logo for our wine bottles. We were looking for something rustic yet modern and simple. We had an idea for beige and cranberry colored wine stained, weathered, imperfect heart. Things that will need to be incorporated into the label design are as follows:
Our last name and also the name of the wine: Fusaldi
The year: 2012
Where is says Alcohol Content on a wine bottle normally write: Alcohol: Deceiving% by vol.
Type of wine: Red Wine
Incorporate our wedding date: Foot Stomped and Bottled for Nadia and Gus's Wedding Day 9/28/13
Wedding

```html
<!DOCTYPE html>
<html lang="en">
<head>
<meta charset="utf-8">
<title>Chateau de la Fusaldi – Vin Rouge Label</title>
<link href="https://fonts.googleapis.com/css2?family=Cinzel:wght@700;900&family=Dancing+Script:wght@400;500&family=Great+Vibes&display=swap" rel="stylesheet">
<style>
  :root {
    --page: #ffffff;
    --cranberry: #4f1850;
    --beige-light: #fffdf3;
    --beige: #f6eecb;
    --beige-deep: #efe2b4;
    --ink: #111111;
    --script-ink: #3c3a76;
    --note-ink: #4a3f7e;
  }
  * { margin: 0; padding: 0; box-sizing: border-box; }
  html, body {
    width: 1025px;
    height: 1200px;
    overflow: hidden;
    background: var(--page);
  }
  .label {
    position: relative;
    width: 1025px;
    height: 1200px;
  }
  .label__art {
    position: absolute;
    inset: 0;
  }
  .label__title {
    position: absolute;
    top: 122px;
    left: 0;
    width: 1025px;
    text-align: center;
    font-family: "Cinzel", serif;
    font-weight: 900;
    font-size: 46px;
    line-height: 62px;
    letter-spacing: 5px;
    color: var(--ink);
  }
  .label__flourish {
    position: absolute;
    top: 186px;
    left: 252px;
    width: 526px;
    height: 30px;
    border-radius: 15px;
    background: radial-gradient(ellipse at center, rgba(17,17,17,0.55) 0%, rgba(17,17,17,0.15) 55%, rgba(17,17,17,0) 100%);
  }
  .label__heart-art {
    position: absolute;
    top: 290px;
    left: 245px;
    width: 490px;
    height: 550px;
    border-radius: 45% 45% 50% 50% / 35% 35% 65% 65%;
    background: radial-gradient(ellipse at 50% 40%, rgba(79,24,80,0) 55%, rgba(79,24,80,0.14) 75%, rgba(79,24,80,0) 100%);
  }
  .dedication {
    position: absolute;
    top: 395px;
    left: 240px;
    width: 500px;
    text-align: center;
    font-family: "Dancing Script", cursive;
    color: var(--script-ink);
    white-space: nowrap;
  }
  .dedication__lead { font-size: 36px; line-height: 46px; }
  .dedication__couple { font-size: 54px; line-height: 84px; }
  .dedication__occasion { font-size: 46px; line-height: 50px; padding-left: 60px; }
  .dedication__date { font-size: 36px; line-height: 66px; padding-left: 44px; }
  .vintage {
    position: absolute;
    top: 700px;
    font-family: "Cinzel", serif;
    font-weight: 900;
    font-size: 56px;
    line-height: 76px;
    letter-spacing: 8px;
    color: var(--ink);
  }
  .vintage--left { left: 180px; }
  .vintage--right { left: 682px; }
  .label__wine-type {
    position: absolute;
    top: 862px;
    left: 0;
    width: 1025px;
    text-align: center;
    font-family: "Great Vibes", cursive;
    font-size: 112px;
    line-height: 130px;
    color: var(--ink);
  }
  .label__abv {
    position: absolute;
    top: 1052px;
    right: 116px;
    font-family: "Dancing Script", cursive;
    font-size: 31px;
    line-height: 42px;
    color: var(--note-ink);
    white-space: nowrap;
  }
</style>
</head>
<body>
<main class="label">
  <svg class="label__art" width="1025" height="1200" viewBox="0 0 1025 1200">
    <defs>
      <radialGradient id="paper-glow" cx="0.5" cy="0.45" r="0.65">
        <stop offset="0" stop-color="var(--beige-light)"/>
        <stop offset="0.55" stop-color="var(--beige)"/>
        <stop offset="1" stop-color="var(--beige-deep)"/>
      </radialGradient>
    </defs>
    <path class="label__paper"
      d="M102,70 L500,74 L947,72 L944,600 L942,1124 L520,1120 L104,1126 L100,600 Z"
      fill="url(#paper-glow)"
      stroke="var(--cranberry)" stroke-width="16" stroke-linejoin="round"/>
    <path class="label__frame-inner"
      d="M112,80 L520,83 L937,82 L934,1114 L114,1116 Z"
      fill="none" stroke="var(--cranberry)" stroke-width="3" opacity="0.5"/>
  </svg>

  <h1 class="label__title">Chateau de la Fusaldi</h1>
  <div class="label__flourish" role="img" aria-label="Decorative scroll flourish beneath the estate name"></div>

  <div class="label__heart-art" role="img" aria-label="Hand-drawn weathered cranberry heart, wine-stained and imperfect"></div>

  <div class="dedication">
    <p class="dedication__lead">Foot Stomped and Bottled for</p>
    <p class="dedication__couple">Nadia &amp; Gus's</p>
    <p class="dedication__occasion">Wedding Day</p>
    <p class="dedication__date">9/28/2013</p>
  </div>

  <p class="vintage vintage--left">2012</p>
  <p class="vintage vintage--right">2012</p>

  <p class="label__wine-type">Vin Rouge</p>
  <p class="label__abv">Alcohol: Deceiving% by Vol.</p>
</main>
</body>
</html>
```